Wix Website design for my therapy business - Willowmere Group

I have started designing a Wix site and have a good idea of what I want.
I have set up the pages, created some design ideas, and inputted the copy. I need someone fabulous to finish off the design aspects. I like working closely with the designers, I was an interior designer in an old career.
I would like the site to be funky but professional. My Wix skills are limited, and I just can't achieve the look I am wanting without having to spend a lot of time learning. If it's easier to start over, that's ok providing you use the same colours, font, images etc. I have included a screenshot of the home page below. I have another site I need to start as soon as we have finished this one.
I am looking for someone who is a good listener and is has design flare. I am easy to get along with and will respond quickly.
I would like to set up SEO and have help in the future.
Let me know if you are the right person for the job.
Target Market(s)
Please needing help with their mental health and for therapy.
Industry/Entity Type
Mental health
Font styles to use
Other font styles liked:
- Futura light
Requirements
Must have
- be easy to navigate and be simple yet stylish
Nice to have
- I have set up the basics of the site - nice to haves are already on the site
Should not have
- old fashioned large chunks of text.

```html
<!DOCTYPE html>
<html lang="en">
<head>
<meta charset="utf-8">
<title>Willowmere Group – Therapy &amp; Counselling</title>
<link href="https://fonts.googleapis.com/css2?family=Jost:wght@300;400;500;600;700&display=swap" rel="stylesheet">
<style>
:root{
  --gold:#a8875a;
  --gold-light:#dcc7a8;
  --sand:#efe8de;
  --grey-bg:#f1f0ee;
  --ink:#262626;
  --body:#555;
  --white:#fff;
}
*{margin:0;padding:0;box-sizing:border-box}
html,body{width:1200px;height:4699px;overflow:hidden}
body{font-family:'Jost',sans-serif;color:var(--ink);background:var(--white);position:relative}
.abs{position:absolute}
.btn{position:absolute;display:flex;align-items:center;justify-content:center;border-radius:30px;font-size:16px;letter-spacing:.3px;text-transform:uppercase;font-weight:400}
.btn-dark{background:var(--ink);color:var(--white)}
.kicker{font-size:20px;color:var(--ink);font-weight:400}
.title{font-size:34px;font-weight:400;color:var(--ink)}
.lead{font-size:14px;line-height:25px;color:var(--body);font-weight:300}

/* header */
.site-header{position:absolute;top:0;left:0;width:1200px;height:70px;background:var(--white)}
.header-phone{left:108px;top:18px;display:flex;align-items:center;gap:10px}
.phone-dot{width:28px;height:28px;border-radius:50%;background:var(--gold);display:flex;align-items:center;justify-content:center}
.header-phone small{display:block;font-size:12px;color:var(--body)}
.header-phone b{display:block;font-size:15px;font-weight:500;letter-spacing:1px}
.brand{left:0;width:1200px;top:18px;text-align:center;font-size:30px;font-weight:500;color:var(--gold)}
.header-contact{left:969px;top:18px;width:122px;height:34px;background:var(--gold);color:var(--white);text-transform:none;font-size:15px}

/* hero */
.hero{position:absolute;top:70px;left:0;width:1200px;height:700px;overflow:hidden}
.hero-photo{position:absolute;inset:0;background:linear-gradient(100deg,#3b5f86 0%,#6d8aa6 30%,#b7a08c 55%,#5f6f43 78%,#3d4d2a 100%)}
.hero-nav{position:absolute;top:22px;left:180px;display:flex;gap:34px;font-size:15px;color:var(--white)}
.hero-nav span:first-child{position:relative}
.hero-nav span:first-child::before{content:"";position:absolute;top:-8px;left:50%;width:4px;height:4px;border-radius:50%;background:var(--white)}
.hero-kicker{left:158px;top:192px;font-size:26px;color:var(--white);font-weight:400}
.hero-title{left:158px;top:240px;font-size:44px;line-height:56px;color:var(--white);font-weight:700;letter-spacing:1px}
.hero-btn{left:158px;top:400px;width:214px;height:48px;background:var(--gold);color:var(--white);font-size:16px}
.hero-arrow{position:absolute;top:286px;width:48px;height:48px;border:2px solid rgba(255,255,255,.8);border-radius:50%}

/* about */
.about-photo{left:0;top:900px;width:470px;height:385px;border-radius:0 200px 200px 0;background:linear-gradient(120deg,#8aa4bf,#c9b48e 55%,#c99a3a)}
.about-band{left:510px;top:930px;width:70px;height:355px;border-radius:0 0 6px 6px;background:var(--gold)}
.about-kicker{left:651px;top:948px}
.about-title{left:651px;top:978px;font-size:36px;line-height:42px}
.about-rule{left:651px;top:1077px;width:60px;height:3px;background:var(--gold)}
.about-text{left:651px;top:1088px;width:380px}
.about-btn{left:651px;top:1220px;width:170px;height:46px}

/* therapy */
.therapy{position:absolute;top:1395px;left:0;width:1200px;height:907px;background:var(--grey-bg)}
.card{position:absolute;top:287px;width:290px;height:434px;background:var(--white);box-shadow:0 4px 18px rgba(0,0,0,.08);overflow:hidden}
.card h3{font-size:18px;font-weight:600;text-align:center;margin-top:38px;letter-spacing:.3px}
.card p{font-size:14px;line-height:21px;color:var(--body);text-align:center;padding:0 34px;margin-top:12px;font-weight:300}
.card-arrow{position:absolute;z-index:2;width:32px;height:32px;border-radius:50%;background:var(--gold);display:flex;align-items:center;justify-content:center}
.card-photo{position:absolute;left:0;width:290px}

/* testimonials */
.testi-photo{left:171px;top:2523px;width:332px;height:355px;background:linear-gradient(180deg,#c6dcef,#e7eef3 60%,#5fb3a3)}
.testi-frame{left:156px;top:2538px;width:332px;height:355px;background:var(--gold-light)}
.stars{left:563px;top:2572px;display:flex;gap:6px;align-items:center}
.testi-text{left:563px;top:2618px;width:360px;font-size:14px;line-height:21px;color:var(--body);font-weight:300}
.avatar{position:absolute;left:988px;width:40px;height:40px;border-radius:50%;background:linear-gradient(135deg,#9a9a9a,#d6d6d6);border:2px solid var(--white);box-shadow:0 2px 6px rgba(0,0,0,.2)}

/* faq */
.faq{position:absolute;top:3019px;left:0;width:1200px;height:520px;background:var(--sand);overflow:hidden}
.faq-title{left:150px;top:114px;width:440px;text-align:center;font-size:26px;line-height:37px;font-weight:600}
.faq-text{left:205px;top:208px;width:330px;text-align:center}
.faq-btn{left:236px;top:307px;width:270px;height:48px;border:2px solid var(--gold);color:var(--ink)}

/* what we do */
.work{position:absolute;top:3539px;left:0;width:1200px;height:766px;overflow:hidden}
.work-bg{position:absolute;inset:0;background:linear-gradient(135deg,#5a4024,#80603c 50%,#6a4d2c)}
.work-title{left:0;width:1200px;top:130px;text-align:center;font-size:28px;color:var(--white);font-weight:600}
.work-text{left:370px;width:460px;top:180px;text-align:center;color:#f1e4d2;font-size:14px;line-height:21px;font-weight:300}
.diamond{position:absolute;top:280px;width:130px;height:130px;transform:rotate(45deg);background:var(--white);border-radius:12px}
.step-label{position:absolute;top:470px;width:220px;text-align:center;color:var(--white);font-size:16px;line-height:22px}
.work-btn{left:772px;top:569px;width:214px;height:48px;background:#f6eadb;color:var(--ink)}

/* footer */
.footer{position:absolute;top:4305px;left:0;width:1200px;height:394px;background:var(--sand)}
.footer-brand{left:110px;top:70px;width:192px;height:92px;background:var(--white);display:flex;align-items:center;justify-content:center;font-size:20px;color:var(--gold);font-weight:500;white-space:nowrap}
.footer-call{left:108px;top:188px;font-size:18px}
.footer-num{left:108px;top:220px;font-size:26px;color:var(--gold);font-weight:600;letter-spacing:1px}
.foot-col{position:absolute;top:80px;padding-left:28px;border-left:2px solid var(--gold-light);height:150px}
.foot-col h4{font-size:15px;color:var(--gold);font-weight:500;letter-spacing:1.5px;margin-bottom:10px}
.foot-col li{list-style:none;font-size:14px;line-height:23px;color:var(--body)}
.contact-row{display:flex;gap:16px;align-items:flex-start;font-size:15px;color:var(--body);margin-bottom:18px;line-height:23px}
.ic{width:30px;height:30px;border-radius:50%;border:1px solid var(--gold);flex:none;display:flex;align-items:center;justify-content:center}
.copy-line{left:0;top:322px;width:1200px;height:1px;background:var(--gold-light)}
.copy{left:108px;top:346px;font-size:14px;color:var(--body)}
.social{position:absolute;top:338px;width:34px;height:34px;border-radius:50%;background:var(--gold)}
</style>
</head>
<body>

<header class="site-header">
  <div class="abs header-phone">
    <span class="phone-dot"><svg width="14" height="14" viewBox="0 0 24 24"><path fill="#fff" d="M6.6 10.8a15 15 0 0 0 6.6 6.6l2.2-2.2c.3-.3.7-.4 1-.2 1.1.4 2.3.6 3.6.6.6 0 1 .4 1 1V20c0 .6-.4 1-1 1A17 17 0 0 1 3 4c0-.6.4-1 1-1h3.5c.6 0 1 .4 1 1 0 1.3.2 2.5.6 3.6.1.3 0 .7-.2 1z"/></svg></span>
    <div><small>24/7 Available</small><b>760-555-0148</b></div>
  </div>
  <div class="abs brand">Willowmere Group</div>
  <div class="btn header-contact">Contact</div>
</header>

<section class="hero">
  <div class="hero-photo" role="img" aria-label="Smiling woman with arms outstretched by a lake and tall grass"></div>
  <nav class="hero-nav"><span>Home</span><span>About Us</span><span>EMDR</span><span>Addictions</span><span>Betrayal Trauma</span><span>PTSD</span><span>Program List</span><span>Resources</span><span>Blog</span></nav>
  <div class="abs hero-kicker">Willowmere Group</div>
  <h1 class="abs hero-title">THERAPY &amp;<br>COUNSELLING</h1>
  <div class="btn hero-btn">Our Services</div>
  <div class="hero-arrow" style="left:61px"><svg width="44" height="44" viewBox="0 0 44 44"><path d="M25 14l-8 8 8 8" stroke="#fff" stroke-width="2" fill="none"/></svg></div>
  <div class="hero-arrow" style="left:1091px"><svg width="44" height="44" viewBox="0 0 44 44"><path d="M19 14l8 8-8 8" stroke="#fff" stroke-width="2" fill="none"/></svg></div>
  <svg class="abs" style="left:0;top:580px" width="1200" height="120" viewBox="0 0 1200 120" preserveAspectRatio="none"><path d="M0 20 C300 -10 700 20 1200 120 L0 120Z" fill="var(--gold-light)"/><path d="M0 40 C300 0 700 40 1200 130 L0 130Z" fill="#fff"/></svg>
</section>

<section class="about">
  <div class="abs about-photo" role="img" aria-label="Woman with windswept hair breathing in the sea air"></div>
  <div class="abs about-band"></div>
  <div class="abs kicker about-kicker">About Us</div>
  <h2 class="abs title about-title">Choose Help.Not<br>Suffering.</h2>
  <div class="abs about-rule"></div>
  <p class="abs lead about-text">Lorem Ipsum is simply dummy text of the printing and typesetting industry. Lorem Ipsum has been the industry's standard dummy text ever since the 1500s, when an unknown printer took a galley of type.</p>
  <div class="btn btn-dark about-btn">Read More</div>
</section>

<section class="therapy">
  <svg class="abs" style="left:0;top:-20px" width="1200" height="70" viewBox="0 0 1200 70" preserveAspectRatio="none"><path d="M0 40 L1200 0 L1200 20 L0 70Z" fill="var(--gold-light)"/></svg>
  <div class="abs kicker" style="left:0;width:1200px;text-align:center;top:142px">Therapy Sessions</div>
  <h2 class="abs title" style="left:0;width:1200px;text-align:center;top:172px;font-size:32px">Specialized Help For Your Mental Health</h2>
  <div class="abs" style="left:1124px;top:187px;width:76px;height:4px;background:var(--gold)"></div>

  <article class="card" style="left:133px">
    <h3>PTSD THERAPY</h3>
    <p>Lorem Ipsum is simply dummy text of the printing and typesetting industry. Lorem Ipsum has been the industry's standard</p>
    <div class="card-arrow" style="left:226px;top:186px"><svg width="12" height="12" viewBox="0 0 12 12"><path d="M3 9l6-6M4 3h5v5" stroke="#fff" stroke-width="1.5" fill="none"/></svg></div>
    <div class="card-photo" style="top:210px;height:224px;background:linear-gradient(180deg,#d9dfe6,#8aa063);border-radius:170px 0 0 0/40px 0 0 0" role="img" aria-label="Woman relaxing outdoors with eyes closed"></div>
  </article>
  <article class="card" style="left:454px;top:282px;height:440px">
    <div class="card-photo" style="top:0;height:170px;background:linear-gradient(120deg,#c9b9a8,#8d8f9a)" role="img" aria-label="Therapist talking with a client"></div>
    <svg class="abs" style="left:0;top:130px" width="290" height="50"><path d="M0 50 C80 0 200 0 290 50Z" fill="#fff"/><path d="M0 50 C80 2 200 2 290 50" stroke="var(--gold)" stroke-width="3" fill="none"/></svg>
    <h3 style="margin-top:186px">EMDR THERAPY</h3>
    <p>Lorem Ipsum is simply dummy text of the printing and typesetting industry. Lorem Ipsum has been the industry's standard</p>
    <div class="card-arrow" style="left:226px;top:383px"><svg width="12" height="12" viewBox="0 0 12 12"><path d="M3 9l6-6M4 3h5v5" stroke="#fff" stroke-width="1.5" fill="none"/></svg></div>
  </article>
  <article class="card" style="left:779px">
    <h3>RELATIONSHIPS</h3>
    <p>Lorem Ipsum is simply dummy text of the printing and typesetting industry. Lorem Ipsum has been the industry's standard</p>
    <div class="card-arrow" style="left:226px;top:186px"><svg width="12" height="12" viewBox="0 0 12 12"><path d="M3 9l6-6M4 3h5v5" stroke="#fff" stroke-width="1.5" fill="none"/></svg></div>
    <div class="card-photo" style="top:210px;height:224px;background:linear-gradient(120deg,#b08a6a,#e2d8cc);border-radius:170px 0 0 0/40px 0 0 0" role="img" aria-label="Smiling couple sitting together"></div>
  </article>
  <div class="btn btn-dark" style="left:508px;top:775px;width:184px;height:48px">Explore More</div>
</section>

<section class="testimonials">
  <div class="abs kicker" style="left:0;width:1200px;text-align:center;top:2407px">Testimonials</div>
  <h2 class="abs title" style="left:0;width:1200px;text-align:center;top:2437px;font-size:32px">Love where you live.</h2>
  <div class="abs" style="left:0;top:2438px;width:82px;height:4px;background:var(--gold)"></div>
  <div class="abs testi-frame"></div>
  <div class="abs testi-photo" role="img" aria-label="Happy woman with arms raised against a bright sky"></div>
  <div class="abs stars">
    <svg width="34" height="26" viewBox="0 0 34 26"><path d="M2 26V14C2 6 6 1 14 0v5c-4 1-6 4-6 8h6v13zM20 26V14c0-8 4-13 12-14v5c-4 1-6 4-6 8h6v13z" fill="var(--gold)"/></svg>
    <span style="color:#e9a300;font-size:18px;letter-spacing:6px;margin-left:10px">★★★★★</span>
  </div>
  <div class="abs testi-text">
    <p>Lorem Ipsum is simply dummy text of the printing and typesetting industry lorem Ipsum..........</p>
    <p style="margin-top:16px">Lorem Ipsum is simply dummy text of the printing and typesetting industry. Lorem Ipsum has been the industry's standard dummy text ever since the 1500s, when an unknown printer took.</p>
    <p style="margin-top:16px;font-size:20px;color:var(--ink);font-weight:400">- DAN R.</p>
  </div>
  <div class="avatar" style="top:2603px" role="img" aria-label="Client portrait"></div>
  <div class="avatar" style="top:2658px;width:50px;height:50px;left:983px;background:linear-gradient(135deg,#8a5b3c,#d3a47c)" role="img" aria-label="Client portrait"></div>
  <div class="avatar" style="top:2724px" role="img" aria-label="Client portrait"></div>
</section>

<section class="faq">
  <svg class="abs" style="left:0;top:0" width="1200" height="520" viewBox="0 0 1200 520"><path d="M0 340 C150 260 350 270 600 150 L600 520 L0 520Z" fill="#fff" opacity=".6"/><path d="M1200 90 L700 90 C640 90 620 200 640 300 C660 420 760 470 860 470 L1200 470Z" fill="var(--gold-light)"/></svg>
  <div class="abs" style="left:648px;top:80px;width:552px;height:378px;border-radius:120px 0 0 170px;background:linear-gradient(180deg,#f3f2ee,#c9d6e6)" role="img" aria-label="Smiling woman in a light blue shirt pointing to the side"></div>
  <h2 class="abs faq-title">Have Questions? Harriet<br>Support Has You Covered.</h2>
  <p class="abs lead faq-text">Lorem Ipsum is simply dummy text of the printing and typesetting industry. Lorem Ipsum has been the industry's standard</p>
  <div class="btn faq-btn">How Can I Help You</div>
  <svg class="abs" style="left:460px;top:366px" width="120" height="50"><path d="M2 4 C0 40 40 44 70 28 C90 18 104 16 116 22" stroke="var(--gold)" stroke-width="1.5" stroke-dasharray="4 4" fill="none"/><path d="M110 16l6 6-8 3" stroke="var(--gold)" stroke-width="1.5" fill="none"/></svg>
</section>

<section class="work">
  <div class="work-bg" role="img" aria-label="Dim room with armchair and houseplants in warm brown tones"></div>
  <svg class="abs" style="left:0;top:0" width="1200" height="100" viewBox="0 0 1200 100" preserveAspectRatio="none"><path d="M0 0 L1200 0 L1200 80 C800 20 400 20 0 30Z" fill="var(--sand)"/></svg>
  <h2 class="abs work-title">What We Do</h2>
  <p class="abs work-text">Lorem Ipsum is simply dummy text of the printing and typesetting industry. Lorem Ipsum has been the industry's standard</p>
  <div class="diamond" style="left:235px"></div>
  <div class="diamond" style="left:535px;background:var(--gold)"></div>
  <div class="diamond" style="left:835px"></div>
  <svg class="abs" style="left:200px;top:260px" width="800" height="200" viewBox="0 0 800 200" fill="none" stroke="#fff" stroke-width="1.5" stroke-dasharray="6 5">
    <path d="M140 50 C200 0 280 0 330 30"/><path d="M440 170 C500 200 570 190 630 150"/>
  </svg>
  <svg class="abs" style="left:266px;top:315px" width="68" height="68" viewBox="0 0 68 68" fill="none" stroke="var(--gold)" stroke-width="2"><rect x="10" y="8" width="34" height="44" rx="3"/><rect x="19" y="4" width="16" height="8" rx="2"/><path d="M17 24h20M17 32h14"/><circle cx="46" cy="48" r="12" fill="#fff"/><path d="M40 48l4 4 8-8"/></svg>
  <svg class="abs" style="left:566px;top:315px" width="68" height="68" viewBox="0 0 68 68" fill="none" stroke="#fff" stroke-width="2"><path d="M14 34h40M24 34v20M44 34v20M8 20v34M60 20v34"/><circle cx="16" cy="14" r="5"/><circle cx="52" cy="14" r="5"/></svg>
  <svg class="abs" style="left:866px;top:315px" width="68" height="68" viewBox="0 0 68 68" fill="none" stroke="var(--gold)" stroke-width="2"><rect x="8" y="8" width="52" height="24"/><path d="M20 44h28l6 16M20 44l-6 16M34 32v12"/></svg>
  <div class="step-label" style="left:190px">Book A<br>Counselling</div>
  <div class="step-label" style="left:490px">Choose A Counselor<br>&amp; Pick A Time</div>
  <div class="step-label" style="left:790px">Relax</div>
  <div class="btn work-btn">Get Started !</div>
  <svg class="abs" style="left:0;top:640px" width="1200" height="126" viewBox="0 0 1200 126" preserveAspectRatio="none"><path d="M0 0 C300 100 800 120 1200 110 L1200 126 L0 126Z" fill="var(--sand)"/></svg>
</section>

<footer class="footer">
  <div class="abs footer-brand">Willowmere Group</div>
  <div class="abs footer-call">Call now for questions</div>
  <div class="abs footer-num">1300 555 010</div>
  <div class="foot-col" style="left:378px"><h4>NAVIGATION</h4><ul><li>Home</li><li>About Us</li><li>EMDR</li><li>Addictions</li><li>Betrayal Trauma</li></ul></div>
  <div class="foot-col" style="left:614px"><h4>NAVIGATION</h4><ul><li>PTSD</li><li>Program List</li><li>Resources</li><li>Blog</li><li>Contact Us</li></ul></div>
  <div class="foot-col" style="left:838px;width:300px"><h4>CONTACT &nbsp;INFORMATION</h4>
    <div class="contact-row"><span class="ic"><svg width="14" height="14" viewBox="0 0 24 24"><path d="M12 2a7 7 0 0 0-7 7c0 5 7 13 7 13s7-8 7-13a7 7 0 0 0-7-7zm0 9.5A2.5 2.5 0 1 1 12 6.5a2.5 2.5 0 0 1 0 5z" fill="var(--gold)"/></svg></span><span>233 Street 111, Suite 1<br>Address, City</span></div>
    <div class="contact-row"><span class="ic"><svg width="14" height="14" viewBox="0 0 24 24"><path fill="var(--gold)" d="M6.6 10.8a15 15 0 0 0 6.6 6.6l2.2-2.2c.3-.3.7-.4 1-.2 1.1.4 2.3.6 3.6.6.6 0 1 .4 1 1V20c0 .6-.4 1-1 1A17 17 0 0 1 3 4c0-.6.4-1 1-1h3.5c.6 0 1 .4 1 1 0 1.3.2 2.5.6 3.6.1.3 0 .7-.2 1z"/></svg></span><span>0400 555 222</span></div>
    <div class="contact-row"><span class="ic"><svg width="14" height="14" viewBox="0 0 24 24"><path fill="var(--gold)" d="M3 5h18v14H3zM3 5l9 7 9-7" stroke="#fff" stroke-width="1.5"/></svg></span><span>name@company.com</span></div>
  </div>
  <div class="abs copy-line"></div>
  <div class="abs copy">Copyright © &nbsp;2023 Willowmere Group. All rights reserved.</div>
  <div class="social" style="left:916px"></div>
  <div class="social" style="left:962px"></div>
  <div class="social" style="left:1008px"></div>
</footer>

</body>
</html>
```